Eye Catching HVAC Display Ad Set

300x250
160x600
100-600
728x90
320x50 Mobile

Flash motion and non-flash

Here is a sample of the type of ad style: http://www.k7partnersco.com/internet-marketing-brindle-hollow/digital-marketing/optometrist/

I'm looking for attractive, high converting display ads in the sizes listed above for the ac repair industry in south florida. The Call To Action number is: (555) 384-2071

This is to attract people with broken air conditioners, hot houses, etc.

Target Market(s)

Homeowners in South Florida with non-working air conditioning.

Industry/Entity Type

Hvac

Font styles to use
Sans Serif

Requirements
Must have
• Call To Action and Phone Number

```html
<!DOCTYPE html>
<html lang="en">
<head>
<meta charset="utf-8">
<title>AC Repair Display Ad Set</title>
<link href="https://fonts.googleapis.com/css2?family=Roboto+Condensed:wght@400;700&display=swap" rel="stylesheet">
<style>
  :root{
    --stage:#3a3b3d;
    --blue-light:#2b6fd6;
    --blue:#1a55b8;
    --blue-dark:#0b3a94;
    --yellow:#ffd21a;
    --white:#ffffff;
    --silver-light:#f4f4f4;
    --silver:#c9c9c9;
    --orange-light:#ffa321;
    --orange:#f86a05;
    --orange-dark:#d94f00;
    --photo-light:#e9edf2;
    --photo-mid:#c7ced8;
    --photo-warm:#8a93a3;
  }
  *{margin:0;padding:0;box-sizing:border-box}
  html,body{width:1200px;height:840px;overflow:hidden}
  body{background:var(--stage);font-family:"Roboto Condensed",Arial,sans-serif;position:relative}
  .ad{position:absolute;overflow:hidden;background:var(--blue);box-shadow:0 3px 8px rgba(0,0,0,.55)}
  .ad svg.panel{position:absolute;left:0;top:0}
  .photo{position:absolute;background:linear-gradient(135deg,var(--photo-light) 0%,var(--photo-mid) 55%,var(--photo-warm) 100%)}
  .copy{position:absolute;text-align:center;color:var(--white);font-weight:700;text-transform:uppercase;line-height:1;text-shadow:0 2px 2px rgba(0,0,0,.35)}
  .copy .y{color:var(--yellow)}
  .copy .sub{text-transform:none;font-weight:700}
  .rule{height:1px;background:rgba(255,255,255,.45);margin:0 auto}
  .cta{position:absolute;display:flex;flex-direction:column;justify-content:center;align-items:center;
       background:linear-gradient(180deg,var(--orange-light) 0%,var(--orange) 55%,var(--orange-dark) 100%);
       border:2px solid rgba(255,255,255,.85);border-radius:10px;color:var(--white);font-weight:400;
       line-height:1.15;text-shadow:0 1px 2px rgba(0,0,0,.35);box-shadow:0 2px 4px rgba(0,0,0,.4)}
  .strip{position:absolute;background:linear-gradient(180deg,var(--silver-light),var(--silver))}

  .skyscraper{left:64px;top:53px;width:192px;height:720px}
  .rect-a{left:278px;top:341px;width:360px;height:300px}
  .rect-b{left:655px;top:341px;width:360px;height:300px}
  .leaderboard{left:278px;top:665px;width:874px;height:108px}
</style>
</head>
<body>

<section class="ad skyscraper">
  <div class="photo" style="left:0;top:0;width:192px;height:300px" role="img" aria-label="Technician smiling while servicing a wall-mounted air conditioner"></div>
  <svg class="panel" width="192" height="720" viewBox="0 0 192 720">
    <defs><radialGradient id="g1" cx="50%" cy="45%" r="70%"><stop offset="0" stop-color="#2b6fd6"/><stop offset="1" stop-color="#0b3a94"/></radialGradient></defs>
    <path d="M0,256 Q70,290 192,250 L192,720 L0,720 Z" fill="url(#g1)"/>
    <path d="M0,256 Q70,290 192,250" fill="none" stroke="#fff" stroke-width="5"/>
  </svg>
  <div class="copy" style="left:0;top:320px;width:192px">
    <div class="y" style="font-size:34px;line-height:1.05">AC Not<br>Working?</div>
    <div class="rule" style="width:160px;margin-top:12px;margin-bottom:12px"></div>
    <div style="font-size:40px">Call Us</div>
    <div style="font-size:31px;margin-top:4px">For Your</div>
    <div class="y" style="font-size:35px;margin-top:4px">AC Repair</div>
    <div class="sub" style="font-size:21px;margin-top:6px">In South Florida</div>
  </div>
  <div class="cta" style="left:13px;top:576px;width:167px;height:67px;font-size:21px"><span>Call Us on</span><span>(555) 384-2071</span></div>
  <div class="strip" style="left:0;top:686px;width:192px;height:34px"></div>
</section>

<section class="ad rect-a">
  <div class="photo" style="left:0;top:0;width:360px;height:150px" role="img" aria-label="Technician smiling while servicing a wall-mounted air conditioner"></div>
  <svg class="panel" width="360" height="300" viewBox="0 0 360 300">
    <defs><radialGradient id="g2" cx="50%" cy="50%" r="70%"><stop offset="0" stop-color="#2b6fd6"/><stop offset="1" stop-color="#0b3a94"/></radialGradient></defs>
    <path d="M0,112 Q140,165 360,130 L360,300 L0,300 Z" fill="url(#g2)"/>
    <path d="M0,112 Q140,165 360,130" fill="none" stroke="#fff" stroke-width="5"/>
  </svg>
  <div class="copy" style="left:0;top:164px;width:360px">
    <div class="y" style="font-size:42px">AC Repair In</div>
    <div class="sub" style="font-size:27px;margin-top:2px">South Florida</div>
  </div>
  <div class="strip" style="left:0;top:266px;width:360px;height:34px"></div>
  <div class="cta" style="left:30px;top:242px;width:302px;height:43px;font-size:22px;border-radius:14px"><span>Call Us on (555) 384-2071</span></div>
</section>

<section class="ad rect-b">
  <div class="photo" style="left:190px;top:0;width:170px;height:300px" role="img" aria-label="Technician smiling while servicing a wall-mounted air conditioner"></div>
  <svg class="panel" width="360" height="300" viewBox="0 0 360 300">
    <defs><radialGradient id="g3" cx="40%" cy="50%" r="70%"><stop offset="0" stop-color="#2b6fd6"/><stop offset="1" stop-color="#0b3a94"/></radialGradient></defs>
    <path d="M0,0 L220,0 Q185,150 232,300 L0,300 Z" fill="url(#g3)"/>
    <path d="M220,0 Q185,150 232,300" fill="none" stroke="#fff" stroke-width="5"/>
  </svg>
  <div class="copy" style="left:0;top:26px;width:198px">
    <div class="y" style="font-size:36px;line-height:1.02">AC Not<br>Working?</div>
    <div class="rule" style="width:170px;margin-top:8px;margin-bottom:8px"></div>
    <div style="font-size:31px">Call Us To</div>
    <div class="y" style="font-size:31px;margin-top:2px">Repair AC</div>
    <div class="sub" style="font-size:21px;margin-top:4px">In South Florida</div>
  </div>
  <div class="cta" style="left:13px;top:209px;width:168px;height:66px;font-size:21px"><span>Call Us on</span><span>(555) 384-2071</span></div>
</section>

<section class="ad leaderboard">
  <div class="photo" style="left:0;top:0;width:290px;height:108px" role="img" aria-label="Technician smiling while servicing a wall-mounted air conditioner"></div>
  <svg class="panel" width="874" height="108" viewBox="0 0 874 108">
    <defs><radialGradient id="g4" cx="50%" cy="50%" r="60%"><stop offset="0" stop-color="#2b6fd6"/><stop offset="1" stop-color="#0b3a94"/></radialGradient></defs>
    <path d="M268,0 Q292,54 270,108 L852,108 L852,0 Z" fill="url(#g4)"/>
    <path d="M268,0 Q292,54 270,108" fill="none" stroke="#fff" stroke-width="5"/>
  </svg>
  <div class="copy" style="left:290px;top:20px;width:370px">
    <div style="font-size:32px">Call Us For <span class="y">AC Repair</span></div>
    <div class="sub" style="font-size:27px;margin-top:5px">In South Florida</div>
  </div>
  <div class="cta" style="left:668px;top:21px;width:166px;height:66px;font-size:21px"><span>Call Us on</span><span>(555) 384-2071</span></div>
  <div class="strip" style="left:852px;top:0;width:22px;height:108px"></div>
</section>

</body>
</html>
```